Event Graphic for Free Community Event

We need a graphic created for a community event that is aimed at families with younger children called Tots Jamboree. This is a free event and has a fair/carnival feel to it with rides, games, and food. I need the graphic to be flexible enough to be able to be modified and used in a variety of ways on different print and digital marketing materials. I also need the centerpiece of the design to be an event logo that can be used as a standalone element.

The overall feel needs to be fun and friendly with a slightly modern edge to it. Attached are some images used in past events. These are for reference only and do not need to be simulated or used in the final product.

Target Market(s)

Families with children

Industry/Entity Type

Church

Font styles to use
Sans Serif

Requirements
Must have
• - Logo that incorporates the event name
- Event Date: September 19 2020
- Event Time: 10am - 2pm
- Church name and logo incorporated: Bright Harbor Community Church (see attached logo files)
Nice to have
• - Bright colors
- Flexible design elements that are interchangeable and scalable for use of the design in different layouts across different mediums and materials.
Should not have
• - Any references or images related to drugs, alcohol, tobacco, or other subjects that would be inappropriate for children.

```html
<!DOCTYPE html>
<html lang="en">
<head>
<meta charset="utf-8">
<title>Tots Jamboree</title>
<link rel="stylesheet" href="https://fonts.googleapis.com/css2?family=Gochi+Hand&family=Poppins:wght@600&display=swap">
<style>
  :root {
    --cream: #fcefdc;
    --pink: #e584b4;
    --yellow: #f5d33b;
    --teal: #b9d9c8;
    --ink: #2a2627;
    --bar-pink: #d264a8;
    --bar-blue: #93c8d0;
    --bar-yellow: #f2cd35;
    --shadow-pink: #e69ac4;
    --shadow-yellow: #f2cf4c;
  }
  html, body {
    margin: 0;
    padding: 0;
    overflow: hidden;
    background: var(--cream);
  }
  .poster {
    position: relative;
    width: 1200px;
    height: 927px;
    overflow: hidden;
    background: var(--cream);
  }
  .backdrop {
    position: absolute;
    inset: 0;
  }
  .church-badge {
    position: absolute;
    left: 518px;
    top: 152px;
    width: 164px;
    height: 164px;
    border-radius: 50%;
    background: var(--ink);
  }
  .church-name {
    position: absolute;
    left: 0;
    width: 1200px;
    top: 334px;
    margin: 0;
    text-align: center;
    font-family: "Gochi Hand", cursive;
    font-weight: 400;
    font-size: 28px;
    color: var(--ink);
  }
  .event-title {
    position: absolute;
    left: 0;
    width: 1200px;
    top: 400px;
    margin: 0;
    text-align: center;
    font-family: "Poppins", sans-serif;
    font-weight: 600;
    font-kerning: none;
    color: #fff;
    -webkit-text-stroke: 2.5px var(--ink);
    paint-order: stroke fill;
    line-height: 1;
  }
  .event-title .line-one {
    display: block;
    font-size: 120px;
    letter-spacing: 14px;
    text-shadow: 5px 6px 0 var(--shadow-pink);
  }
  .event-title .line-two {
    display: block;
    margin-top: 15px;
    font-size: 64px;
    letter-spacing: 8px;
    text-shadow: 4px 5px 0 var(--shadow-yellow);
  }
  .color-bar {
    position: absolute;
    left: 446px;
    top: 721px;
    width: 306px;
    height: 19px;
    display: flex;
  }
  .color-bar span { flex: 1; }
  .color-bar .seg-pink { background: var(--bar-pink); }
  .color-bar .seg-blue { background: var(--bar-blue); }
  .color-bar .seg-yellow { background: var(--bar-yellow); }
  .event-when {
    position: absolute;
    left: 0;
    width: 1200px;
    top: 764px;
    margin: 0;
    text-align: center;
    font-family: "Gochi Hand", cursive;
    font-size: 36px;
    line-height: 46px;
    color: var(--ink);
  }
</style>
</head>
<body>
<main class="poster">
  <svg class="backdrop" width="1200" height="927" viewBox="0 0 1200 927" role="img" aria-label="Playful background of large pink, yellow and mint triangles with scattered small doodles">
    <polygon class="shape-pink" points="0,0 462,0 222,927 156,927 0,603" fill="var(--pink)"/>
    <polygon class="shape-yellow" points="618,122 1200,240 1200,735" fill="var(--yellow)"/>
    <polygon class="shape-teal" points="709,629 829,927 305,927" fill="var(--teal)"/>
  </svg>

  <div class="church-badge"></div>
  <p class="church-name">Bright Harbor Community Church</p>

  <h1 class="event-title">
    <span class="line-one">TOTS</span>
    <span class="line-two">JAMBOREE</span>
  </h1>

  <div class="color-bar">
    <span class="seg-pink"></span>
    <span class="seg-blue"></span>
    <span class="seg-yellow"></span>
  </div>

  <p class="event-when">September 19 2020<br>10am - 2pm</p>
</main>
</body>
</html>
```